RZO Design tag

Looking to design a tag for our new hat & glove brand RZO Design. These are winter hats & gloves. Long story short these are lower cost/retail items but I'm trying to convey higher quality goods through a nice tag. I’ve attached a tag of another brand we have to give you a general idea of what I’d be looking for- but again for our new brand RZO Design.
I’m thinking we can do one general design- and then do it in 4 different color schemes: First one mimicking the attachment’s colors for ladies items- so a few different shades of pink. Then 2nd color scheme a darker more masculine color tone for mens or unisex items- maybe blue/dark blue, and then a 3rd color scheme for kids items that is more vibrant/kid like colors. Last one red & green for some Christmas items we do.
A few things:
• Trying to make the tags look classy as possible
• The tag will need to measure 2.25” high x 2” wide. The top little bit would have to be space left blank for a hole punch- just like on the attached sample tag. But again the tags designed would need to be 2.25" tall x 2" wide so not the same shape as the sample tag.
• For item name you can just put “Knit Hat” for the generic tag item name (in place of what says on the same “Chenille Slipper Bootie”). Please try to keep the writing a nice font similar to what is on this tag- again trying to have a classy tag look
• On the bottom center (In place of Made in China) it would just need to say “One Size” in standard font
Hope this helps & thank you
Target Market(s)
People buying winter hats & gloves
Industry/Entity Type
Retail- winter hats & gloves
Look and feel

```html
<!DOCTYPE html>
<html lang="en">
<head>
<meta charset="utf-8">
<title>Knit Hat Tags</title>
<link href="https://fonts.googleapis.com/css2?family=Yellowtail&family=Jost:wght@400&display=swap" rel="stylesheet">
<style>
  :root {
    --backdrop: #258371;
    --tag-paper: #ebe4dd;
    --tag-edge: #8a8a86;
    --hole: #5b5b5b;
    --size-text: #5a5a58;

    --xmas-red: #a30d0d;
    --xmas-green: #2b5a12;
    --ladies-deep: #c85252;
    --ladies-soft: #e38582;
    --mens-navy: #3b526b;
    --mens-blue: #2f7597;
    --kids-pink: #f0609d;
    --kids-aqua: #4fd3d3;
    --kids-lilac: #c98cee;
  }
  html, body {
    margin: 0;
    padding: 0;
    width: 1107px;
    height: 1200px;
    overflow: hidden;
    background: var(--backdrop);
  }
  .sheet {
    position: relative;
    width: 1107px;
    height: 1200px;
  }
  .tag {
    position: absolute;
    width: 359px;
    height: 404px;
    box-sizing: border-box;
    background: var(--tag-paper);
    border: 1px solid var(--tag-edge);
    box-shadow: -10px 14px 14px rgba(20, 60, 50, 0.45);
    overflow: hidden;
  }
  .tag--christmas { left: 182px; top: 171px; }
  .tag--ladies    { left: 583px; top: 171px; }
  .tag--mens      { left: 182px; top: 618px; }
  .tag--kids      { left: 583px; top: 618px; }

  .tag__hole {
    position: absolute;
    left: 50%;
    top: 19px;
    width: 36px;
    height: 36px;
    margin-left: -18px;
    border-radius: 50%;
    background: var(--hole);
  }
  .tag__name {
    position: absolute;
    margin: 0;
    font-family: "Yellowtail", "Brush Script MT", cursive;
    font-weight: 400;
    font-size: 106px;
    line-height: 1;
    white-space: nowrap;
  }
  .tag__name--first  { left: 44px; top: 132px; }
  .tag__name--second { left: 94px; top: 210px; }
  .tag__size {
    position: absolute;
    left: 0;
    right: 0;
    top: 360px;
    margin: 0;
    text-align: center;
    font-family: "Jost", sans-serif;
    font-size: 19px;
    letter-spacing: 0.3px;
    color: var(--size-text);
  }

  .tag--christmas .initial { color: var(--xmas-red); }
  .tag--christmas .rest    { color: var(--xmas-green); }
  .tag--ladies .initial    { color: var(--ladies-deep); }
  .tag--ladies .rest       { color: var(--ladies-soft); }
  .tag--mens .initial      { color: var(--mens-navy); }
  .tag--mens .rest         { color: var(--mens-blue); }
  .tag--kids .initial      { color: var(--kids-pink); }
  .tag--kids .rest         { color: var(--kids-aqua); }
  .tag--kids .rest--lilac  { color: var(--kids-lilac); }
</style>
</head>
<body>
<main class="sheet">

  <section class="tag tag--christmas" aria-label="Christmas knit hat tag">
    <span class="tag__hole"></span>
    <p class="tag__name tag__name--first"><span class="initial">K</span><span class="rest">nit</span></p>
    <p class="tag__name tag__name--second"><span class="initial">H</span><span class="rest">at</span></p>
    <p class="tag__size">ONE SIZE</p>
  </section>

  <section class="tag tag--ladies" aria-label="Ladies knit hat tag">
    <span class="tag__hole"></span>
    <p class="tag__name tag__name--first"><span class="initial">K</span><span class="rest">nit</span></p>
    <p class="tag__name tag__name--second"><span class="initial">H</span><span class="rest">at</span></p>
    <p class="tag__size">ONE SIZE</p>
  </section>

  <section class="tag tag--mens" aria-label="Mens knit hat tag">
    <span class="tag__hole"></span>
    <p class="tag__name tag__name--first"><span class="initial">K</span><span class="rest">nit</span></p>
    <p class="tag__name tag__name--second"><span class="initial">H</span><span class="rest">at</span></p>
    <p class="tag__size">ONE SIZE</p>
  </section>

  <section class="tag tag--kids" aria-label="Kids knit hat tag">
    <span class="tag__hole"></span>
    <p class="tag__name tag__name--first"><span class="initial">K</span><span class="rest">nit</span></p>
    <p class="tag__name tag__name--second"><span class="initial">H</span><span class="rest rest--lilac">at</span></p>
    <p class="tag__size">ONE SIZE</p>
  </section>

</main>
</body>
</html>
```